engaging mobile application to encourage lifestyle change

We need an App that will help people get from Bold 4 Bloom. A weight loss program based on realistic and healthy lifestyle modifications. By learning portion control, healthy food choices, and with the encouragement to get moving.
We would like the design to be gender neutral but must be fun.
The final design must be easy to use and useful to our clients.

Target Market(s)

Health, Wellbeing, Weightloss

Industry/Entity Type

Weight

Font styles to use
Sans Serif

Requirements
Must have
• Hydration log, Weigh-ins with fat %, Food log, Location of meetings,lectures and weigh-ins, list of restaurants that comply with B4B, Fitness plan, Mall walk maps, daily motivational message.

```html
<!DOCTYPE html>
<html lang="en">
<head>
<meta charset="utf-8">
<title>Lifestyle Tracker Screens</title>
<link rel="stylesheet" href="https://fonts.googleapis.com/css2?family=Montserrat:wght@300;400;500&display=swap">
<style>
  :root {
    --canvas: #f7f7f7;
    --screen: #ffffff;
    --ink: #4a5060;
    --ink-soft: #6b6f78;
    --muted: #a3a6ac;
    --faint: #e4e5e8;
    --water: #1ea7dd;
    --weight: #f04e4e;
    --food: #2dbb4a;
  }
  * { box-sizing: border-box; margin: 0; padding: 0; }
  html, body { width: 1200px; height: 1000px; overflow: hidden; }
  body {
    background: var(--canvas);
    font-family: "Montserrat", "Helvetica Neue", Arial, sans-serif;
    color: var(--ink);
    position: relative;
  }
  .screen {
    position: absolute;
    top: 210px;
    width: 325px;
    height: 580px;
    background: var(--screen);
    overflow: hidden;
    box-shadow: 0 1px 3px rgba(0,0,0,0.06);
  }
  .screen--hydration { left: 50px; }
  .screen--weight { left: 440px; }
  .screen--food { left: 831px; }

  .status-bar {
    position: absolute; top: 3px; left: 5px; right: 5px; height: 14px;
    font-size: 9.5px; font-weight: 500; color: #111;
    display: flex; align-items: center; justify-content: space-between;
  }
  .status-bar__left, .status-bar__right { display: flex; align-items: center; gap: 3px; width: 90px; }
  .status-bar__right { justify-content: flex-end; }
  .status-bar__signal { letter-spacing: -1px; font-size: 7px; }

  .nav { position: absolute; top: 27px; left: 0; right: 0; height: 20px; }
  .nav__menu { position: absolute; left: 15px; top: 4px; }
  .nav__title {
    text-align: center; font-size: 13.5px; font-weight: 500; color: var(--ink-soft);
    line-height: 20px;
  }

  .centered { position: absolute; transform: translateX(-50%); text-align: center; white-space: nowrap; }
  .date { top: 74px; left: 50%; font-size: 12px; color: var(--muted); font-weight: 300; }

  .big-value { font-size: 53px; font-weight: 300; color: var(--ink); line-height: 1; }
  .big-label { font-size: 19px; font-weight: 300; color: var(--muted); }
  .caps-label { font-size: 14px; font-weight: 300; letter-spacing: 0.5px; color: var(--muted); }

  .axis {
    position: absolute; top: 226px; left: 9px; right: 9px;
    display: grid; grid-template-columns: repeat(7, 1fr);
    font-size: 11.5px; font-weight: 300; color: var(--muted);
  }
  .axis span { text-align: center; }
  .axis__item--active { font-weight: 500; }
  .screen--hydration .axis__item--active { color: var(--water); }
  .screen--weight .axis__item--active { color: var(--weight); }
  .screen--food .axis__item--active { color: var(--food); }

  .chart { position: absolute; left: 0; top: 250px; width: 325px; height: 218px; }

  .footer-value { font-size: 24px; font-weight: 300; color: var(--muted); line-height: 1; }
  .footer-value--strong { color: var(--ink-soft); }
  .footer-label { font-size: 12px; font-weight: 300; color: var(--muted); margin-top: 8px; }

  .divider { position: absolute; left: 164px; top: 85px; width: 2px; height: 103px; }
  .divider__top { height: 40px; background: var(--faint); }
  .divider__bottom { height: 63px; background: var(--water); }

  .goal { position: absolute; left: 48px; top: 416px; color: var(--muted); }
  .goal__value { font-size: 25px; font-weight: 300; line-height: 1; }
  .goal__label { font-size: 12px; font-weight: 300; margin-left: 3px; }

  .calorie-stack { top: 104px; left: 50%; height: 60px; width: 200px; }
  .calorie-stack__ghost { position: absolute; left: 0; right: 0; font-size: 60px; font-weight: 300; color: #ecedef; letter-spacing: 8px; line-height: 1; }
  .calorie-stack__main { position: absolute; left: 0; right: 0; font-size: 60px; font-weight: 300; color: var(--ink); line-height: 1; }

  .remaining { position: absolute; right: 26px; top: 433px; font-size: 20px; font-weight: 300; color: #8a9494; }
  .add-button { position: absolute; left: 226px; top: 502px; }
</style>
</head>
<body>

<section class="screen screen--hydration">
  <div class="status-bar">
    <div class="status-bar__left"><span class="status-bar__signal">●●●●●</span><span>Nimbus</span>
      <svg width="11" height="8" viewBox="0 0 11 8"><path d="M5.5 8 L1 3 A6.5 6.5 0 0 1 10 3 Z" fill="#111"/></svg></div>
    <span>9:41 AM</span>
    <div class="status-bar__right"><span>100%</span>
      <svg width="22" height="9" viewBox="0 0 22 9"><rect x="0.5" y="0.5" width="19" height="8" rx="1.5" fill="none" stroke="#111"/><rect x="2" y="2" width="16" height="5" fill="#111"/><rect x="20.5" y="3" width="1.5" height="3" fill="#111"/></svg></div>
  </div>
  <header class="nav">
    <svg class="nav__menu" width="14" height="12" viewBox="0 0 14 12"><path d="M0 1h14M0 6h14M0 11h14" stroke="#333" stroke-width="1.5"/></svg>
    <h1 class="nav__title">Hydration Log</h1>
  </header>

  <div class="centered" style="left:83px; top:95px;">
    <div class="big-value">60%</div>
    <div class="big-label" style="margin-top:10px;">hydrated</div>
  </div>
  <div class="divider"><div class="divider__top"></div><div class="divider__bottom"></div></div>
  <div class="centered" style="left:243px; top:95px;">
    <div class="big-value">2,4L</div>
    <div class="big-label" style="margin-top:10px;">target</div>
  </div>

  <nav class="axis">
    <span>SUN</span><span>MON</span><span>TUE</span><span>WED</span><span>THU</span><span class="axis__item--active">FRI</span><span>SAT</span>
  </nav>

  <svg class="chart" viewBox="0 0 325 218" aria-label="Daily water intake chart">
    <defs>
      <linearGradient id="waterFill" x1="0" y1="0" x2="0" y2="1">
        <stop offset="0" stop-color="#7ccbef"/>
        <stop offset="1" stop-color="#eef9fd"/>
      </linearGradient>
    </defs>
    <path d="M0 88 C40 95 80 112 105 100 C120 92 130 85 142 92 C158 104 168 148 185 150 C200 152 205 120 218 117 C232 114 238 80 253 79 L325 80 L325 218 L0 218 Z" fill="url(#waterFill)"/>
    <circle cx="253" cy="34" r="14" fill="#dcdcdc"/>
    <text x="253" y="37.5" text-anchor="middle" font-size="9" fill="#555" font-family="Montserrat, sans-serif">2,4L</text>
    <circle cx="253" cy="79" r="15" fill="var(--water)"/>
    <text x="253" y="82.5" text-anchor="middle" font-size="9" fill="#fff" font-family="Montserrat, sans-serif">1,8L</text>
  </svg>

  <div class="centered" style="left:86px; top:504px;">
    <div class="footer-value">13:30</div>
    <div class="footer-label">Last Drink</div>
  </div>
  <div class="centered" style="left:237px; top:504px;">
    <div class="footer-value footer-value--strong">15:30
      <svg width="20" height="20" viewBox="0 0 20 20" style="vertical-align:-2px; margin-left:2px;"><circle cx="10" cy="11" r="7.5" fill="none" stroke="var(--water)" stroke-width="1.4"/><path d="M10 7v4l2.5 2" fill="none" stroke="var(--water)" stroke-width="1.4"/><path d="M2 5 L5 2 M18 5 L15 2" stroke="var(--water)" stroke-width="1.4"/></svg></div>
    <div class="footer-label">Next Drink</div>
  </div>
</section>

<section class="screen screen--weight">
  <div class="status-bar">
    <div class="status-bar__left"><span class="status-bar__signal">●●●●●</span><span>Nimbus</span>
      <svg width="11" height="8" viewBox="0 0 11 8"><path d="M5.5 8 L1 3 A6.5 6.5 0 0 1 10 3 Z" fill="#111"/></svg></div>
    <span>9:41 AM</span>
    <div class="status-bar__right"><span>100%</span>
      <svg width="22" height="9" viewBox="0 0 22 9"><rect x="0.5" y="0.5" width="19" height="8" rx="1.5" fill="none" stroke="#111"/><rect x="2" y="2" width="16" height="5" fill="#111"/><rect x="20.5" y="3" width="1.5" height="3" fill="#111"/></svg></div>
  </div>
  <header class="nav">
    <svg class="nav__menu" width="14" height="12" viewBox="0 0 14 12"><path d="M0 1h14M0 6h14M0 11h14" stroke="#333" stroke-width="1.5"/></svg>
    <h1 class="nav__title">Weight Loss</h1>
  </header>

  <div class="centered date">Today, 14 Feb 2016</div>
  <div class="centered" style="left:50%; top:102px;">
    <div class="big-value" style="font-size:62px;">60<span style="font-size:26px;">kg</span></div>
    <div class="caps-label" style="margin-top:8px;">BODY WEIGHT</div>
  </div>

  <nav class="axis">
    <span>SEP</span><span>OCT</span><span>NOV</span><span>DEC</span><span>JAN</span><span class="axis__item--active">FEB</span><span>MAR</span>
  </nav>

  <svg class="chart" viewBox="0 0 325 218" aria-label="Monthly body weight chart">
    <defs>
      <linearGradient id="weightFill" x1="0" y1="0" x2="0" y2="1">
        <stop offset="0" stop-color="#f08a8a"/>
        <stop offset="1" stop-color="#fde9e9"/>
      </linearGradient>
    </defs>
    <path d="M0 12 C90 30 150 45 200 85 C225 105 240 122 255 127 L325 127 L325 218 L0 218 Z" fill="url(#weightFill)"/>
    <line x1="155" y1="184" x2="325" y2="184" stroke="var(--weight)" stroke-width="1.2"/>
    <circle cx="255" cy="127" r="15" fill="var(--weight)"/>
    <text x="255" y="130.5" text-anchor="middle" font-size="9" fill="#fff" font-family="Montserrat, sans-serif">60kg</text>
  </svg>
  <div class="goal">
    <div class="goal__value">50kg</div>
    <div class="goal__label">goals</div>
  </div>

  <div class="centered" style="left:87px; top:504px;">
    <div class="footer-value">55 kg</div>
    <div class="footer-label">Max Weight</div>
  </div>
  <div class="centered" style="left:237px; top:504px;">
    <div class="footer-value footer-value--strong">48 kg</div>
    <div class="footer-label">Min Weight</div>
  </div>
</section>

<section class="screen screen--food">
  <div class="status-bar">
    <div class="status-bar__left"><span class="status-bar__signal">●●●●●</span><span>Nimbus</span>
      <svg width="11" height="8" viewBox="0 0 11 8"><path d="M5.5 8 L1 3 A6.5 6.5 0 0 1 10 3 Z" fill="#111"/></svg></div>
    <span>9:41 AM</span>
    <div class="status-bar__right"><span>100%</span>
      <svg width="22" height="9" viewBox="0 0 22 9"><rect x="0.5" y="0.5" width="19" height="8" rx="1.5" fill="none" stroke="#111"/><rect x="2" y="2" width="16" height="5" fill="#111"/><rect x="20.5" y="3" width="1.5" height="3" fill="#111"/></svg></div>
  </div>
  <header class="nav">
    <svg class="nav__menu" width="14" height="12" viewBox="0 0 14 12"><path d="M0 1h14M0 6h14M0 11h14" stroke="#333" stroke-width="1.5"/></svg>
    <h1 class="nav__title">Food Log</h1>
  </header>

  <div class="centered date">Today, 14 Feb 2016</div>
  <div class="centered calorie-stack">
    <div class="calorie-stack__ghost">2000</div>
    <div class="calorie-stack__main">750</div>
  </div>
  <div class="centered caps-label" style="left:50%; top:174px;">CALORIES</div>

  <nav class="axis">
    <span>6AM</span><span>9AM</span><span>12PM</span><span>3PM</span><span>6PM</span><span class="axis__item--active">9PM</span><span>12AM</span>
  </nav>

  <svg class="chart" viewBox="0 0 325 218" aria-label="Calories through the day chart">
    <defs>
      <linearGradient id="foodFill" x1="0" y1="0" x2="0" y2="1">
        <stop offset="0" stop-color="#8eea98"/>
        <stop offset="1" stop-color="#e8f9f4"/>
      </linearGradient>
    </defs>
    <path d="M0 192 C60 185 110 170 150 130 C180 98 195 60 212 56 L240 52 L325 53 L325 218 L0 218 Z" fill="url(#foodFill)"/>
    <g fill="#4fcf63">
      <circle cx="27" cy="190" r="4.5"/><circle cx="47" cy="186" r="4.5"/>
      <circle cx="67" cy="181" r="4.5"/><circle cx="82" cy="176" r="4.5"/>
      <circle cx="107" cy="164" r="4.5"/><circle cx="134" cy="146" r="4.5"/>
      <circle cx="158" cy="127" r="4.5"/><circle cx="177" cy="103" r="4.5"/>
      <circle cx="191" cy="81" r="4.5"/>
    </g>
    <circle cx="212" cy="56" r="15" fill="var(--food)"/>
    <text x="212" y="59.5" text-anchor="middle" font-size="9" fill="#fff" font-family="Montserrat, sans-serif">120</text>
  </svg>
  <div class="remaining">1250 remaining</div>

  <div class="centered" style="left:87px; top:504px;">
    <div class="footer-value">120cal</div>
    <div class="footer-label">Prev Food</div>
  </div>
  <svg class="add-button" width="52" height="52" viewBox="0 0 52 52" aria-label="Add food">
    <circle cx="26" cy="26" r="25" fill="none" stroke="#3a3f4a" stroke-width="1.2"/>
    <path d="M26 13v26M13 26h26" stroke="#3a3f4a" stroke-width="1.2"/>
  </svg>
</section>

</body>
</html>
```